Film Production Company Needs HTML Website Design

My production company, VelvetHarborMediaWorks.com , needs to have an HTML design of our website. I would like a minotaur as the company symbol, as well as a hellfire in the background. Something dark and edgy, like we currently have, but different. The password to open the attached zip file is: FBLY7cqu94Obm15HNwYa
Please check out our website and include all of the tabs that are currently in the design, especially the Investor section.

Film Production

```html
<!DOCTYPE html>
<html lang="en">
<head>
<meta charset="utf-8">
<title>Velvet Harbor Productions</title>
<link rel="stylesheet" href="https://fonts.googleapis.com/css2?family=Cinzel:wght@700&family=Marcellus&family=Tinos&family=Open+Sans&display=swap">
<style>
  :root {
    --page: #ffffff;
    --black: #000000;
    --ember: #5a0a02;
    --ember-deep: #2a0400;
    --glow: #b01a05;
    --gold: #f2b21c;
    --gold-soft: #f6e2a6;
    --red-text: #e0242a;
    --orange-text: #f0a040;
    --sprocket: #4a0a06;
  }
  * { margin: 0; padding: 0; box-sizing: border-box; }
  html, body { width: 1200px; height: 1000px; overflow: hidden; background: var(--page); }
  .site {
    position: absolute; left: 50px; top: 37px; width: 1108px; height: 920px;
    background:
      radial-gradient(ellipse 60% 45% at 50% 45%, #3a0602 0%, transparent 70%),
      linear-gradient(180deg, #000 0 115px, #3d0702 125px, #1e0301 330px, #0d0100 700px, #000 820px);
    overflow: hidden;
  }
  .brand { position: absolute; left: 0; right: 0; top: 38px; text-align: center; }
  .brand-name {
    font-family: "Cinzel", serif; font-weight: 700; font-size: 62px;
    color: var(--gold); letter-spacing: 1px; line-height: 1;
  }
  .brand-sub {
    margin-top: 42px; margin-left: 90px; font-family: "Tinos", serif; font-size: 21px;
    color: var(--red-text); letter-spacing: 24px;
  }
  .main-nav {
    position: absolute; left: 7px; top: 201px; width: 1081px; height: 50px;
    background: var(--black); border-radius: 10px;
    box-shadow: 0 0 0 3px #3a0603, 0 0 14px 4px var(--glow);
    display: flex; align-items: center; padding-left: 100px;
  }
  .main-nav a {
    font-family: "Marcellus", serif; font-size: 19px; letter-spacing: 1.5px;
    text-decoration: none; color: var(--red-text); padding: 0 36px;
    border-right: 1px solid #3a3a3a; line-height: 22px;
  }
  .main-nav a:last-child { border-right: none; }
  .main-nav a.alt { color: var(--gold); }
  .panel {
    position: absolute; border-radius: 8px;
    background: linear-gradient(180deg, #300500 0%, #110100 45%, #000 100%);
    box-shadow: inset 0 0 0 2px #3b0602, 0 0 12px 3px #4a0802;
  }
  .about { left: 12px; top: 268px; width: 370px; height: 557px; padding: 38px 20px 0 33px; }
  .panel-title {
    font-family: "Tinos", serif; font-size: 30px; letter-spacing: -2px;
    color: var(--gold); line-height: 1;
  }
  .about .panel-title { margin-left: 5px; margin-bottom: 8px; }
  .about p {
    font-family: "Marcellus", serif; font-size: 11px; line-height: 14.8px;
    color: var(--gold-soft); margin-bottom: 15px; letter-spacing: 0.2px;
  }
  .hero-art {
    position: absolute; left: 392px; top: 262px; width: 320px; height: 585px;
    background:
      radial-gradient(ellipse 35% 45% at 50% 48%, #f49a1c 0%, #d04a08 35%, #6a1202 65%, transparent 85%),
      radial-gradient(ellipse 50% 10% at 50% 94%, #ff8a10 0%, transparent 80%);
  }
  .works { left: 806px; top: 271px; width: 284px; height: 270px; }
  .works .panel-title { text-align: center; margin-top: 18px; font-size: 33px; }
  .film-strip {
    position: absolute; left: 37px; top: 76px; width: 205px; height: 143px;
    background: #0a0000; display: grid; grid-template-columns: 1fr 1fr; grid-template-rows: 1fr 1fr;
    padding: 0 16px; border-left: 12px solid #1a0200; border-right: 12px solid #1a0200;
  }
  .film-strip span {
    display: flex; align-items: center; justify-content: center;
    font-family: "Tinos", serif; font-size: 21px; letter-spacing: -1.5px; color: var(--orange-text);
  }
  .more-link {
    position: absolute; right: 16px; bottom: 17px; padding: 2px 9px;
    border-radius: 8px; background: #2a0502;
    font-family: "Open Sans", sans-serif; font-size: 9.5px; color: var(--gold-soft);
  }
  .productions { left: 806px; top: 558px; width: 287px; height: 270px; }
  .productions .panel-title { text-align: center; margin-top: 20px; font-size: 26px; }
  .reel {
    position: absolute; left: 20px; top: 60px; width: 255px; height: 150px;
    background: radial-gradient(ellipse 50% 50% at 50% 30%, #3a0702, #0a0000 80%);
  }
  .sprockets { position: absolute; top: 12px; display: flex; flex-direction: column; gap: 9px; }
  .sprockets i { display: block; width: 24px; height: 20px; border-radius: 3px; background: var(--sprocket); }
  .sprockets.left { left: 5px; }
  .sprockets.right { right: 5px; }
  .reel-caption {
    position: absolute; left: 0; right: 0; top: 56px; text-align: center;
    font-family: "Marcellus", serif; font-size: 12px; color: var(--orange-text);
  }
  .reel-nav { position: absolute; left: 52px; top: 224px; width: 170px; display: flex; justify-content: space-between; }
  .social { position: absolute; left: 22px; top: 864px; display: flex; gap: 10px; }
  .social span { width: 32px; height: 32px; background: #1a1208; display: block; }
  .copyright {
    position: absolute; left: 0; right: 0; top: 873px; text-align: center;
    font-family: "Open Sans", sans-serif; font-size: 10px; color: var(--orange-text);
  }
</style>
</head>
<body>
<div class="site">
  <header class="brand">
    <div class="brand-name">VELVET HARBOR</div>
    <div class="brand-sub">PRODUCTIONS</div>
  </header>

  <nav class="main-nav">
    <a href="#">Home</a>
    <a href="#" class="alt">About Us</a>
    <a href="#">News</a>
    <a href="#">Productions</a>
    <a href="#">Investors</a>
    <a href="#">Contact Us</a>
  </nav>

  <section class="panel about">
    <h2 class="panel-title">ABOUT US</h2>
    <p>Sed laoreet aliquam leo ut tellus dolor dapi eget elementum vel cursus elei fend eliter Aenean auctor wisi et urna aliquam erat volutpat. Duis ac turpis. Integer rutrum ante eu lacus. Sed laoreet aliquam leo ut tellus dolor dapi eget elementum vel cursus elei fend eliter Aenean auctor wisi et urna aliquam erat volutp</p>
    <p>Sed laoreet aliquam leo ut tellus dolor dapi eget elementum vel cursus elei fend eliter Aenean auctor wisi et urna aliquam erat volutp<br>Sed laoreet aliquam leo<br>&nbsp;ut tellus dolor dapi eget elementum vel<br>cursus elei fend<br>eliter Aenean auctor wisi et urna aliquam erat volutp<br>Sed laoreet aliquam leo ut tellus d<br>olor dapi eget elementum vel cursus elei fend eliter Aenean auctor wisi et urna<br>aliquam erat volutp</p>
    <p>Sed laoreet aliquam leo ut tellus dolor dapi eget elementum vel cursus elei fend eliter Aenean auctor wisi et urna aliquam erat volutp</p>
    <p>Sed laoreet aliquam leo ut tellus dolor dapi eget elementum vel cursus elei fend eliter Aenean auctor wisi et urna aliquam erat volutp<br>Sed laoreet aliquam leo ut tellus dolor dapi eget elementum vel cursus elei fend eliter Aenean auctor wisi et urna aliquam erat volutp</p>
  </section>

  <div class="hero-art" role="img" aria-label="Minotaur warrior holding an axe, standing in roaring hellfire"></div>

  <section class="panel works">
    <h2 class="panel-title">LATEST WORKS</h2>
    <div class="film-strip">
      <span>PHOTO</span><span>PHOTO</span><span>PHOTO</span><span>PHOTO</span>
    </div>
    <a class="more-link">More gallery &rsaquo;</a>
  </section>

  <section class="panel productions">
    <h2 class="panel-title">OUR PRODUCTIONS</h2>
    <div class="reel">
      <div class="sprockets left"><i></i><i></i><i></i><i></i><i></i></div>
      <div class="sprockets right"><i></i><i></i><i></i><i></i><i></i></div>
      <div class="reel-caption">PICTURE OF PRODUCTIONS</div>
    </div>
    <div class="reel-nav">
      <svg width="10" height="14" viewBox="0 0 10 14"><path d="M7 2 L2 7 L7 12" fill="none" stroke="#e8d0b0" stroke-width="2"/></svg>
      <svg width="10" height="14" viewBox="0 0 10 14"><path d="M3 2 L8 7 L3 12" fill="none" stroke="#e8d0b0" stroke-width="2"/></svg>
    </div>
  </section>

  <footer>
    <div class="social" aria-label="Social links">
      <span></span><span></span><span></span><span></span>
    </div>
    <p class="copyright">Velvet Harbor &copy; 2014 . Privacy Policy</p>
  </footer>
</div>
</body>
</html>
```